Revise my existing consulting brief with new logo

I just got a logo from Plume Forge for my new management consulting business, and would like to add it to my existing consulting brief, both 1 and 2 page versions, and would like to improve the layout of these documents to make them look more professional. These documents are essentially the brochure or flyer for my business, so they need to be easy to read and understand quickly. I would like these to be either ppt or Word format so that I can update wording in future, and so that I can save to pdf when I want to share with prospective clients. My new logo print file is attached here, as well as the consulting brief documents that need new layout.
Colors and layout used in the revised consulting brief that you will produce should be aligned to the new logo
Updates

Many of you proposed designs that took into account just one of the 2 documents I sent. However, please be advised that I am looking for designs for both documents that I sent, which are 1- and 2-paged versions of my consulting brief, which is essentially a flyer or brochure that explains my consulting service.

This should not look like a resume, but should be more attractive as a kind of business flyer/brochure.

Please also be aware that I am open to landscape format designs, not just portrait, which would be more in line with the versions I sent you.

Target Market(s)

Pharmaceutical and medical device companies

Industry/Entity Type

Pharmaceutical and medical device

Font styles to use
Serif
Sans Serif

Requirements
Must have
• Color and look that align to my new logo. Ability for me to update the text later on my own as needed, so that I can adapt it to different clients.
Should not have
• I am not looking for a PowerPoint template or stationary to match my logo. I am just looking to have the consulting briefs that I sent revised so that they fit the new logo and look more professional in layout.

```html
<!DOCTYPE html>
<html lang="en">
<head>
<meta charset="utf-8">
<title>Northpath Advisory – Consulting Brief</title>
<link href="https://fonts.googleapis.com/css2?family=Poppins:wght@400;600;700;800&family=Lato:ital,wght@0,400;0,700;1,400&display=swap" rel="stylesheet">
<style>
  :root{
    --navy:#11398c;
    --teal:#1bb9b5;
    --bar:#3f62c4;
    --bar-dark:#3551b0;
    --row:#dce4f4;
    --ink:#1b1b1b;
    --on-teal:#ffffff;
    --summary:#4a62b0;
    --white:#ffffff;
    --canvas:#ececec;
  }
  *{box-sizing:border-box;margin:0;padding:0}
  html,body{width:1200px;height:572px;overflow:hidden;background:var(--canvas)}
  body{position:relative;font-family:"Lato",sans-serif;color:var(--ink)}

  .page{position:absolute;top:37px;width:750px;height:1060px;background:var(--white);
        transform:scale(.4667);transform-origin:0 0;overflow:hidden}
  .page--one{left:42px}
  .page--two{left:437px}
  .page--three{left:815px}

  .page-shapes{position:absolute;inset:0;width:750px;height:1060px}

  .identity{position:absolute;left:0;top:36px;width:328px;text-align:center;color:var(--white)}
  .identity__name{font-family:"Poppins",sans-serif;font-weight:700;font-size:27px;line-height:1.1}
  .identity__role{font-family:"Lato",sans-serif;font-size:12.5px;letter-spacing:.3px}

  .portrait{position:absolute;left:56px;top:93px;width:216px;height:216px;border-radius:50%;
            border:3px solid var(--teal);
            background:radial-gradient(circle at 50% 38%,#e8b49c 0 22%,#b4542c 40%,#6a5a34 72%,#43482a 100%)}

  .brand{position:absolute;left:338px;top:72px;display:flex;align-items:center;gap:14px}
  .brand__mark{width:54px;height:54px;border-radius:50%;background:var(--teal);flex:none}
  .brand__name{font-family:"Poppins",sans-serif;font-weight:800;color:var(--navy);
               font-size:36px;line-height:1.02;text-transform:uppercase}

  .taglines{position:absolute;left:338px;top:188px;font-family:"Poppins",sans-serif;
            font-size:14.5px;color:var(--navy);line-height:16px;list-style:none}
  .taglines li{display:flex;align-items:center;gap:8px}
  .taglines svg{width:11px;height:11px}

  .contact{position:absolute;left:338px;top:231px;width:390px;font-family:"Poppins",sans-serif;
           font-size:14px;color:var(--navy);line-height:23px;white-space:nowrap}
  .contact__line{display:flex;align-items:center;gap:7px}
  .contact__phone{font-weight:600;margin-right:10px}
  .contact svg{width:14px;height:14px;flex:none}
  .contact .square{width:12px;height:12px;border:2px solid var(--navy);border-radius:2px;flex:none}

  /* page one */
  .intro{position:absolute;left:43px;top:352px;width:236px;font-size:15.5px;line-height:20.2px;color:var(--ink)}
  .smallcaps{font-variant:small-caps;letter-spacing:.4px}

  .capabilities{position:absolute;border-collapse:collapse;background:var(--row);font-size:13px;line-height:17px}
  .capabilities caption{background:var(--bar);color:var(--white);text-align:left;padding:4px 8px;
                        font-size:15.5px;letter-spacing:1px}
  .capabilities caption.blank{height:18px;padding:0}
  .capabilities td{vertical-align:top;padding:3px 6px 3px 7px;border-bottom:2px solid var(--white)}
  .capabilities th{vertical-align:top;text-align:left;font-weight:700;padding:3px 6px 3px 7px;border-bottom:2px solid var(--white)}
  .capabilities ul{padding-left:20px}
  .capabilities li{padding-left:2px}
  .page--one .capabilities{left:347px;top:332px;width:382px}
  .page--one .capabilities th{width:130px}

  /* page two */
  .section-bar{position:absolute;background:var(--bar-dark);color:var(--white);font-size:16px;
               padding:1px 5px;letter-spacing:.3px;font-weight:400}
  .page--two .section-bar{left:44px;top:353px;width:243px}
  .about{position:absolute;left:44px;top:385px;width:246px;font-size:13.6px;line-height:17.6px;color:var(--on-teal)}
  .about p{margin-bottom:10px}

  .achievements{position:absolute;left:348px;top:330px;width:382px;background:var(--row);font-size:13px;line-height:17px}
  .achievements__head{background:var(--bar);color:var(--white);font-weight:700;font-size:14px;
                      line-height:18.5px;padding:2px 7px;text-align:justify;text-align-last:left}
  .achievements ul{list-style:none}
  .achievements li{position:relative;padding:7px 8px 10px 30px;border-bottom:2px solid var(--white)}
  .achievements li::before{content:"";position:absolute;left:10px;top:13px;width:5px;height:5px;border-radius:50%;background:var(--ink)}

  /* page three */
  .summary{position:absolute;left:344px;top:308px;width:330px;font-size:13px;line-height:17.4px;color:var(--summary)}
  .summary .smallcaps{font-size:17px}
  .page--three .section-bar{left:42px;top:358px;width:243px}
  .about-list{position:absolute;left:42px;top:382px;width:245px;font-size:13.6px;line-height:18.6px;padding-left:23px;color:var(--on-teal)}
  .about-list li{margin-bottom:2px;padding-left:6px}
  .page--three .capabilities{left:346px;top:437px;width:366px}
  .page--three .capabilities th{width:104px}
</style>
</head>
<body>

<!-- ======== Page 1 ======== -->
<section class="page page--one">
  <svg class="page-shapes" viewBox="0 0 750 1060" aria-hidden="true">
    <polygon points="0,0 750,0 750,35 349,35 324,105 324,200 0,328" fill="var(--navy)"/>
    <polygon points="0,328 324,200 324,955 150,1060 0,1060" fill="var(--teal)"/>
  </svg>
  <header class="identity">
    <h1 class="identity__name">Claire Martell</h1>
    <p class="identity__role">INDEPENDENT CONSULTANT</p>
  </header>
  <div class="portrait" role="img" aria-label="Portrait photo of the consultant"></div>
  <div class="brand"><span class="brand__mark"></span><span class="brand__name">Northpath<br>Advisory LLC</span></div>
  <ul class="taglines">
    <li><svg viewBox="0 0 12 12"><rect x=".75" y=".75" width="10.5" height="10.5" fill="none" stroke="currentColor" stroke-width="1.3"/><path d="M3 6l2 2 4-4.5" fill="none" stroke="currentColor" stroke-width="1.4"/></svg>Solving Complex Challenges</li>
    <li><svg viewBox="0 0 12 12"><rect x=".75" y=".75" width="10.5" height="10.5" fill="none" stroke="currentColor" stroke-width="1.3"/><path d="M3 6l2 2 4-4.5" fill="none" stroke="currentColor" stroke-width="1.4"/></svg>Driving Programs from Strategy to Action</li>
  </ul>
  <div class="contact">
    <div class="contact__line"><svg viewBox="0 0 14 14"><rect x="0" y="2" width="14" height="10" rx="1.5" fill="currentColor"/><path d="M1 3l6 5 6-5" fill="none" stroke="#fff" stroke-width="1.3"/></svg>martell.claire@mailbox.net</div>
    <div class="contact__line"><svg viewBox="0 0 14 14"><circle cx="7" cy="7" r="7" fill="currentColor"/><path d="M4.5 3.5l1.5 1.6-.8 1.2c.6 1.2 1.3 1.9 2.5 2.5l1.2-.8 1.6 1.5-1 1.2c-2.8-.3-5.3-2.8-6-6z" fill="#fff"/></svg><span class="contact__phone">555 014 0192</span><span class="square"></span>www.prolink.net/in/c-martell</div>
  </div>

  <p class="intro"><span class="smallcaps">Claire Martell</span> helps companies tackle and succeed in making change by providing project leadership and program management services for key business objectives. She understands the importance of getting it right the first time, and specializes in shaping solutions to drive complex business initiatives from strategy to action.</p>

  <table class="capabilities">
    <caption>EXPERTISE AND CAPABILITIES:</caption>
    <tr><th>Mergers and Acquisitions</th><td><ul>
      <li>For companies acquiring a target: Build integration teams, lead team in developing integration plan &amp; budget, facilitate planning for an efficient and effective Day 1, and for 30-60-90 day horizon</li>
      <li>Assist companies looking to be acquired to prepare their people, processes and systems for due diligence</li></ul></td></tr>
    <tr><th>Inflation Reduction Act</th><td><ul>
      <li>Drug price negotiation operational readiness: Put in place process and governance for submission development and ensuing engagements with the agency. Identify cross-functional team members needed, design approval processes, build and oversee integrated project plan and timeline.</li>
      <li>Part D redesign readiness: Identify gaps and develop plan to address, including chartering workstreams and creation and implementation of plans and timelines to drive from strategy to execution</li></ul></td></tr>
    <tr><th>Strategic Programs &amp; Business Transformation</th><td><ul>
      <li>Develop strategy, framework and governance to accomplish organization and business model change, inclusive of people, processes and systems</li>
      <li>Change Management for new ways of working and new business models</li>
      <li>Facilitate goal-setting and strategic prioritization exercises with leadership teams</li></ul></td></tr>
  </table>
</section>

<!-- ======== Page 2 ======== -->
<section class="page page--two">
  <svg class="page-shapes" viewBox="0 0 750 1060" aria-hidden="true">
    <polygon points="0,0 750,0 750,35 349,35 324,105 324,200 0,328" fill="var(--navy)"/>
    <polygon points="0,328 324,200 324,955 150,1060 0,1060" fill="var(--teal)"/>
  </svg>
  <header class="identity">
    <h1 class="identity__name">Claire Martell</h1>
    <p class="identity__role">INDEPENDENT CONSULTANT</p>
  </header>
  <div class="portrait" role="img" aria-label="Portrait photo of the consultant"></div>
  <div class="brand"><span class="brand__mark"></span><span class="brand__name">Northpath<br>Advisory LLC</span></div>
  <ul class="taglines">
    <li><svg viewBox="0 0 12 12"><rect x=".75" y=".75" width="10.5" height="10.5" fill="none" stroke="currentColor" stroke-width="1.3"/><path d="M3 6l2 2 4-4.5" fill="none" stroke="currentColor" stroke-width="1.4"/></svg>Solving Complex Challenges</li>
    <li><svg viewBox="0 0 12 12"><rect x=".75" y=".75" width="10.5" height="10.5" fill="none" stroke="currentColor" stroke-width="1.3"/><path d="M3 6l2 2 4-4.5" fill="none" stroke="currentColor" stroke-width="1.4"/></svg>Driving Programs from Strategy to Action</li>
  </ul>
  <div class="contact">
    <div class="contact__line"><svg viewBox="0 0 14 14"><rect x="0" y="2" width="14" height="10" rx="1.5" fill="currentColor"/><path d="M1 3l6 5 6-5" fill="none" stroke="#fff" stroke-width="1.3"/></svg>martell.claire@mailbox.net</div>
    <div class="contact__line"><svg viewBox="0 0 14 14"><circle cx="7" cy="7" r="7" fill="currentColor"/><path d="M4.5 3.5l1.5 1.6-.8 1.2c.6 1.2 1.3 1.9 2.5 2.5l1.2-.8 1.6 1.5-1 1.2c-2.8-.3-5.3-2.8-6-6z" fill="#fff"/></svg><span class="contact__phone">555 014 0192</span><span class="square"></span>www.prolink.net/in/c-martell</div>
  </div>

  <h2 class="section-bar">About Claire Martell:</h2>
  <div class="about">
    <p>As a passionate executive with 25 years of Pharmaceutical and MedTech expertise at Halden &amp; Rowe, Claire is now helping companies achieve business results by providing leadership and oversight for key objectives and initiatives. She brings clarity to the complex and pioneers the way forward to solve new problems, leading critical business programs to rapid and seamless execution.</p>
    <p>Ms. Martell is known for uncovering new solutions, connecting the dots, building strong cross-functional relationships, and driving engagement across teams.</p>
    <p>Claire leverages her robust marketing background to enhance strategic transformations by infusing customer-centric insights, effective communication, and commercial focus. Her marketing roles included product development and launch, global portfolio management, managing alliances for innovative external partnerships and KOL development.</p>
    <p>Ms. Martell is a dual citizen of France and the US, and has lived and worked on two continents. She leverages her cross-cultural know-how to advance business collaboration and business goals.</p>
  </div>

  <div class="achievements">
    <p class="achievements__head">Claire has held leadership roles in Marketing, M&amp;A, Business Transformation and Strategy &amp; Operations. Her achievements include :</p>
    <ul>
      <li><b>Directed enterprise-wide integration</b> team accountable for integrating a foot &amp; ankle implants company into H&amp;R: transitioned from distributors to direct sales force, doubled production, met quality remediation goals, orchestrated organizational structure &amp; technology changes, and moved customer service and distribution.</li>
      <li><b>Led integration</b> and new business model implementation of a critical asset in the Joint Reconstruction space that resulted in increased product pull-through, exceeding deal model expectations by double digits</li>
      <li>Drove business readiness and company response to the unprecedented changes stemming from the Inflation Reduction Act. Led operations for 2 drug price negotiation submissions to the agency. Created and facilitated program of 6 workstreams, leading IRA transformation activities.<br>&nbsp;</li>
      <li><b>Strategy &amp; Ops lead for launch</b> of company's first CAR-T cell therapy. Dove in deep with a series of workshops to define launch plan and interdependencies, designed and implemented team structure and project governance, navigated changing landscape and unforeseen challenges, resulting in a best-in-class launch that has become a role model in the cell and gene therapy space.</li>
      <li><b>As Strategic Business</b> Transformation lead for US Oncology business, orchestrated strategy and operations excellence, including business goal-setting, strategic planning process, leadership business reviews and oversight of launch planning for 5 new drugs.</li>
    </ul>
  </div>
</section>

<!-- ======== Page 3 ======== -->
<section class="page page--three">
  <svg class="page-shapes" viewBox="0 0 750 1060" aria-hidden="true">
    <polygon points="0,0 750,0 750,35 349,35 324,105 324,200 0,328" fill="var(--navy)"/>
    <polygon points="0,328 324,200 324,955 150,1060 0,1060" fill="var(--teal)"/>
  </svg>
  <header class="identity">
    <h1 class="identity__name">Claire Martell</h1>
    <p class="identity__role">INDEPENDENT CONSULTANT</p>
  </header>
  <div class="portrait" role="img" aria-label="Portrait photo of the consultant"></div>
  <div class="brand"><span class="brand__mark"></span><span class="brand__name">Northpath<br>Advisory LLC</span></div>
  <ul class="taglines">
    <li><svg viewBox="0 0 12 12"><rect x=".75" y=".75" width="10.5" height="10.5" fill="none" stroke="currentColor" stroke-width="1.3"/><path d="M3 6l2 2 4-4.5" fill="none" stroke="currentColor" stroke-width="1.4"/></svg>Solving Complex Challenges</li>
    <li><svg viewBox="0 0 12 12"><rect x=".75" y=".75" width="10.5" height="10.5" fill="none" stroke="currentColor" stroke-width="1.3"/><path d="M3 6l2 2 4-4.5" fill="none" stroke="currentColor" stroke-width="1.4"/></svg>Driving Programs from Strategy to Action</li>
  </ul>
  <div class="contact">
    <div class="contact__line"><svg viewBox="0 0 14 14"><rect x="0" y="2" width="14" height="10" rx="1.5" fill="currentColor"/><path d="M1 3l6 5 6-5" fill="none" stroke="#fff" stroke-width="1.3"/></svg>martell.claire@mailbox.net</div>
    <div class="contact__line"><svg viewBox="0 0 14 14"><circle cx="7" cy="7" r="7" fill="currentColor"/><path d="M4.5 3.5l1.5 1.6-.8 1.2c.6 1.2 1.3 1.9 2.5 2.5l1.2-.8 1.6 1.5-1 1.2c-2.8-.3-5.3-2.8-6-6z" fill="#fff"/></svg><span class="contact__phone">555 014 0192</span><span class="square"></span>www.prolink.net/in/c-martell</div>
  </div>

  <p class="summary"><span class="smallcaps">Claire Martell</span> helps companies tackle and succeed in making change by providing project leadership and program management services for key business objectives. She understands the importance of getting it right the first time and specializes in shaping solutions to drive complex business initiatives from strategy to action.</p>

  <h2 class="section-bar">About Claire</h2>
  <ul class="about-list">
    <li>25 years of Pharmaceutical and MedTech expertise at Halden &amp; Rowe</li>
    <li>Robust strategy and marketing background</li>
    <li>Enhances business transformations by infusing customer-centric insights, effective communication, and commercial focus.</li>
    <li>Uncovers new solutions, connects the dots, builds strong cross-functional relationships, and drives engagement across teams.</li>
  </ul>

  <table class="capabilities">
    <caption class="blank"></caption>
    <tr><th>Inflation Reduction Act</th><td><ul>
      <li>Drug price negotiation operational readiness: Put in place process and governance for submission development and ensuing engagements with the agency. Identify cross-functional team members needed, design approval processes, lead change management, build and oversee integrated project plan and timeline.</li>
      <li>Part D redesign readiness: Identify gaps and develop plan to address, including chartering workstreams and creation and implementation of plans and timelines to drive from strategy to execution</li></ul></td></tr>
    <tr><th>Mergers &amp; Acquisitions</th><td><ul>
      <li>For companies acquiring a target: Build integration teams, lead team in developing integration plan &amp; budget, facilitate planning for an efficient and effective Day 1, and for 30-60-90-day horizon</li>
      <li>Assist companies looking to be acquired to prepare their people, processes and systems for due diligence</li></ul></td></tr>
    <tr><th>Strategic Programs &amp; Business Transformation</th><td><ul>
      <li>Develop strategy, framework and governance to accomplish organization and business model change, inclusive of people, processes and systems</li>
      <li>Change Management for new ways of working and new business models</li>
      <li>Facilitate goal-setting and strategic prioritization exercises with leadership teams</li></ul></td></tr>
  </table>
</section>

</body>
</html>
```